Website design for new health & wellness company

We need our website to be designed in a user friendly way. Needs to be aesthetically pleasing to viewer and easy to navigate and upload content for our small team . The logo should be completely redesigned , please do not reference the current one thats on our site for a starting place. (included below though) We want to move away from that.

the website is : www.brightpathforward.com

We are a small group of writers/coaches who believe that to change the world you have to be the change and we provide tips/suggestions for every day life that if followed can make a huge difference in your life and overall being.

Target Market(s)

Men and women ages 22 to 50

Industry/Entity Type

Health And Wellness

Logo Text

Cultivate the life of your dreams

Coding

Coded - Design and coding required

Number of Pages Required

3 page

Font styles to use
Sans Serif

Colors

Designer to choose colors to be used in the design.

Requirements
Must have
• Easy to navigate. Mobile friendly. Gender neutral, should appeal to both.

```html
<!DOCTYPE html>
<html lang="en">
<head>
<meta charset="UTF-8">
<title>Healthy Lifestyle Blog</title>
<link rel="stylesheet" href="https://fonts.googleapis.com/css2?family=Open+Sans:wght@300;400;600&family=Parisienne&display=swap">
<style>
  :root {
    --sky: #66d1de;
    --sky-text: #4fc6d4;
    --mist: #ececec;
    --ink: #666666;
    --white: #ffffff;
    --night: #262626;
    --leaf: #347a27;
    --rule: #dcdcdc;
  }
  * { margin: 0; padding: 0; box-sizing: border-box; }
  html, body { width: 1036px; height: 1200px; overflow: hidden; }
  body { position: relative; font-family: "Open Sans", Arial, sans-serif; background: var(--mist); }

  .top-rule { position: absolute; left: 0; top: 0; width: 1036px; height: 4px; background: var(--rule); }

  .articles { position: absolute; left: 0; top: 4px; width: 1036px; height: 638px; background: var(--sky); }
  .site-title { position: absolute; left: 0; width: 100%; top: 26px; text-align: center; color: var(--white); font-weight: 400; font-size: 47px; letter-spacing: 0.5px; }
  .site-tagline { position: absolute; left: 0; width: 100%; top: 80px; text-align: center; color: var(--white); font-family: "Parisienne", cursive; font-size: 33px; font-weight: 400; }

  .photo { position: absolute; }
  .feature-photo { left: 108px; top: 160px; width: 344px; height: 445px; background: linear-gradient(160deg, #8a9c6e 0%, #d88a70 50%, #b9634e 100%); }
  .card-photo { width: 225px; height: 148px; }
  .photo-fitness { left: 469px; top: 160px; background: linear-gradient(135deg, #8e8a86, #3e6f9e); }
  .photo-food { left: 706px; top: 160px; width: 222px; background: linear-gradient(135deg, #5a4a3e, #d8d2cc); }
  .photo-group { left: 469px; top: 400px; width: 220px; height: 152px; background: linear-gradient(135deg, #6e6a66, #b04a40); }
  .photo-juice { left: 706px; top: 400px; width: 223px; height: 154px; background: linear-gradient(135deg, #8a7a6e, #c96a3c); }

  .tag { position: absolute; background: var(--white); color: var(--sky-text); font-size: 10.5px; line-height: 15px; padding: 0 7px; border-radius: 8px; text-transform: uppercase; }
  .tag-square { border-radius: 0; }

  .caption { position: absolute; width: 225px; text-align: center; color: var(--white); font-size: 13.5px; line-height: 18px; }

  .consult-photo { left: 125px; top: 692px; width: 257px; height: 402px; background: linear-gradient(180deg, #7a6e66 0%, #776a5e 60%, #8a7a3a 100%); }
  .consult-slogan { position: absolute; left: 125px; top: 862px; width: 257px; text-align: center; color: var(--white); font-size: 29px; line-height: 35px; text-transform: uppercase; }

  .consult-title { position: absolute; left: 460px; top: 700px; color: var(--ink); font-weight: 300; font-size: 29px; letter-spacing: 0.3px; }
  .consult-text { position: absolute; left: 462px; top: 760px; width: 460px; color: var(--ink); font-size: 11.5px; line-height: 15.5px; }

  .field { position: absolute; width: 198px; height: 26px; background: var(--white); border: none; font-family: "Open Sans", Arial, sans-serif; font-size: 11.5px; color: #9a9a9a; padding-left: 10px; line-height: 26px; }
  .send-button { position: absolute; left: 565px; top: 1042px; width: 229px; height: 44px; border-radius: 22px; background: var(--leaf); color: var(--white); font-size: 16px; text-align: center; line-height: 44px; box-shadow: 2px 3px 4px rgba(0,0,0,0.35); }

  .site-footer { position: absolute; left: 0; top: 1146px; width: 1036px; height: 54px; background: var(--night); }
  .copyright { position: absolute; left: 113px; top: 18px; color: var(--white); font-size: 11.5px; }
  .social { position: absolute; top: 15px; left: 769px; display: flex; gap: 8px; }
  .social span { width: 22px; height: 22px; border-radius: 50%; background: #e3e3e3; display: block; }
</style>
</head>
<body>
  <div class="top-rule"></div>

  <section class="articles">
    <h1 class="site-title">Awesome Articles</h1>
    <p class="site-tagline">Your Healthy Lifestyle Blog</p>

    <div class="photo feature-photo" role="img" aria-label="Smiling woman in a hat holding a green smoothie"></div>
    <span class="tag tag-square" style="left:118px; top:167px;">Blogging</span>

    <div class="photo card-photo photo-fitness" role="img" aria-label="Woman stretching on a blue yoga mat"></div>
    <span class="tag" style="left:475px; top:167px;">Fitness</span>
    <p class="caption" style="left:469px; top:322px;">How 30 minutes a day can<br>make you healtheir</p>

    <div class="photo card-photo photo-food" role="img" aria-label="Table with strawberries, grapefruit and breakfast plates"></div>
    <span class="tag" style="left:716px; top:167px;">Health</span>
    <p class="caption" style="left:705px; top:322px;">10 ways to ring more<br>balance into your life</p>

    <div class="photo photo-group" role="img" aria-label="Group of friends laughing together in a studio"></div>
    <span class="tag" style="left:475px; top:411px;">Health</span>
    <span class="tag" style="left:546px; top:411px;">Self love</span>
    <p class="caption" style="left:469px; top:566px;">How 30 minutes a day can<br>make you healtheir</p>

    <div class="photo photo-juice" role="img" aria-label="Woman at a kitchen counter with fresh juices and fruit"></div>
    <span class="tag" style="left:716px; top:411px;">Health</span>
    <span class="tag" style="left:858px; top:411px;">Travel</span>
    <p class="caption" style="left:705px; top:566px;">10 ways to ring more<br>balance into your life</p>
  </section>

  <section class="consultation">
    <div class="photo consult-photo" role="img" aria-label="Smiling woman in a mustard top"></div>
    <p class="consult-slogan">Change<br>your health<br>in one day</p>

    <h2 class="consult-title">REQUEST A FREE CONSULTATION</h2>
    <p class="consult-text">Send me an loream ipsum a few words about what you are looking to achieve loream can schedule a FREE initial consultation to discuss your health history and goals.</p>

    <div class="field" style="left:462px; top:838px;">Your Name</div>
    <div class="field" style="left:712px; top:838px;">Your e-mail</div>
    <div class="field" style="left:462px; top:930px;">Message</div>
    <div class="field" style="left:712px; top:930px;">Contact No.</div>

    <div class="send-button">Send Message</div>
  </section>

  <footer class="site-footer">
    <p class="copyright">Copyright ©2016 all rights reserved</p>
    <div class="social" aria-label="Social links">
      <span></span><span></span><span></span><span></span><span></span>
    </div>
  </footer>
</body>
</html>
```